Cybersecurity company is looking for business card.

I need a business card design for our company, we are a cybersecurity company providing advance technology to protect agains any kind of malware. We need a fresh modern design it should communicate modern, technology and growth.

Target Market(s)

Business to business

Industry/Entity Type

Business

Contact Information for Business Card

Should have location, address, fax, mobile, phone, email and website.

Requirements
Must have
• Must follow company's logo color and style. Must have the company's log on its.

```html
<!DOCTYPE html>
<html lang="en">
<head>
<meta charset="UTF-8">
<title>Vantrel Business Card</title>
<link rel="stylesheet" href="https://fonts.googleapis.com/css2?family=Roboto:wght@300;400;700&family=Crimson+Text:ital@1&display=swap">
<style>
  :root {
    --brand-red: #a81f24;
    --brand-red-dark: #8e171c;
    --card-white: #ffffff;
    --card-grey: #f1f1f1;
    --ink: #2b2b2b;
    --ink-soft: #555555;
    --icon: #6a6a6a;
    --rule: #c9c9c9;
    --page: #e4e4e4;
  }
  * { margin: 0; padding: 0; box-sizing: border-box; }
  html, body {
    width: 1200px; height: 900px; overflow: hidden;
    background: var(--page);
  }
  .canvas {
    position: relative; width: 1200px; height: 900px;
  }
  .card {
    position: absolute; left: 250px; width: 700px; height: 400px;
    overflow: hidden;
    box-shadow: 0 6px 18px rgba(0,0,0,0.18);
  }
  .card--front { top: 40px; background: var(--brand-red); }
  .card--back { top: 470px; background: var(--card-grey); }
  .card__art { position: absolute; inset: 0; display: block; }

  .logo-word {
    font-family: "Roboto", Arial, sans-serif;
    font-weight: 700; font-size: 96px; letter-spacing: -2px;
    fill: var(--ink);
  }

  .accent-bar {
    position: absolute; left: 92px; top: 0;
    width: 72px; height: 218px; background: var(--brand-red);
  }
  .identity {
    position: absolute; left: 92px; top: 228px;
    font-family: "Roboto", Arial, sans-serif; color: var(--ink);
  }
  .identity__name { font-size: 27px; line-height: 1; letter-spacing: 0.5px; }
  .identity__first { font-weight: 700; }
  .identity__last { font-weight: 300; }
  .identity__role {
    margin-top: 4px; font-size: 15px; font-weight: 400;
    color: var(--ink-soft); letter-spacing: 0.5px;
  }

  .contact {
    position: absolute; left: 402px; top: 140px;
    padding: 6px 0 6px 16px; border-left: 1px solid var(--rule);
    list-style: none;
  }
  .contact__item {
    display: flex; align-items: center; height: 31px;
    font-family: "Crimson Text", Georgia, serif; font-style: italic;
    font-size: 18px; color: var(--ink-soft);
  }
  .contact__icon {
    display: block; position: static;
    width: 16px; height: 16px; margin-right: 16px;
    fill: var(--icon); flex: none;
  }
</style>
</head>
<body>
<main class="canvas">

  <section class="card card--front" aria-label="Card front">
    <svg class="card__art" width="700" height="400" viewBox="0 0 700 400">
      <defs>
        <linearGradient id="redShade" x1="0" y1="0" x2="1" y2="1">
          <stop offset="0" stop-color="#b52228"/>
          <stop offset="1" stop-color="#921a1f"/>
        </linearGradient>
      </defs>
      <rect width="700" height="400" fill="url(#redShade)"/>
      <g transform="rotate(-27 350 200)">
        <rect x="-250" y="125" width="1200" height="140" fill="var(--card-white)"/>
        <line x1="-250" y1="275" x2="950" y2="275" stroke="var(--card-white)" stroke-width="3"/>
        <text class="logo-word" x="350" y="232" text-anchor="middle">vantrel</text>
      </g>
    </svg>
  </section>

  <section class="card card--back" aria-label="Card back">
    <div class="accent-bar"></div>

    <div class="identity">
      <p class="identity__name"><span class="identity__first">NAME</span> <span class="identity__last">SURNAME</span></p>
      <p class="identity__role">DESIGNATION</p>
    </div>

    <ul class="contact">
      <li class="contact__item">
        <svg class="contact__icon" viewBox="0 0 16 16" aria-hidden="true"><path d="M3.5 1l2.5 3-1.5 1.6c.8 2 2.3 3.6 4.4 4.4L10.5 8.5l3 2.5-1.2 2.6C7 13.2 2.8 9 2.4 3.7z"/></svg>
        (000) 000-0000
      </li>
      <li class="contact__item">
        <svg class="contact__icon" viewBox="0 0 16 16" aria-hidden="true"><rect x="4" y="1" width="8" height="4"/><rect x="1" y="5.5" width="14" height="6.5" rx="1"/><rect x="4.5" y="9.5" width="7" height="5" fill="#ffffff" stroke="#6a6a6a"/></svg>
        (000) 000-0000
      </li>
      <li class="contact__item">
        <svg class="contact__icon" viewBox="0 0 16 16" aria-hidden="true"><rect x="1" y="3" width="14" height="10"/><path d="M1 3l7 6 7-6" fill="none" stroke="#ffffff" stroke-width="1.4"/></svg>
        name@companyname.com
      </li>
      <li class="contact__item">
        <svg class="contact__icon" viewBox="0 0 16 16" aria-hidden="true"><circle cx="8" cy="8" r="7"/><path d="M1 8h14M8 1c-3 3.5-3 10.5 0 14M8 1c3 3.5 3 10.5 0 14" fill="none" stroke="#ffffff" stroke-width="1"/></svg>
        www.companyname.com
      </li>
      <li class="contact__item">
        <svg class="contact__icon" viewBox="0 0 16 16" aria-hidden="true"><path d="M8 1a5 5 0 0 0-5 5c0 3.8 5 9 5 9s5-5.2 5-9a5 5 0 0 0-5-5z"/><circle cx="8" cy="6" r="1.8" fill="#ffffff"/></svg>
        address
      </li>
    </ul>
  </section>

</main>
</body>
</html>
```